Regenerative Wellness Flyer to recruit Dr offices and clinics

This is a flyer that will be used to recruit new Dr offices and clinics to make them aware of a brand new product that is about to hit the market.

I uploaded an older flyer that I do like. This product is not Stem Cells but fixes a lot of the same things. So the title could be Regenerative Wellness and Cell Factor Therapy.

I also loaded a multiple page info on the product.

I would like to be able to change out logo's & contact information as I have a couple sales people helping push this. I also attached my logo, Quenmora. Would like to be able to a QR code...

This is the landing page that the flyer will drive Dr's to:
https://app.brivantopage.com/v2/preview/K3TrwBnqLZmdUx8hPsVe?notrack=true

Target Market(s)

Dr's office, clinics, alternative wellness clinics

Industry/Entity Type

health & wellness

Colors
0054AA
0677BA
7BADD7
CADEEF
E8F1F8
00AB8E
00BBA5
67D7C9
C6EFE9
E9F9F6

Requirements
Nice to have
• The ability to change out the logo/contact info areas

```html
<!DOCTYPE html>
<html lang="en">
<head>
<meta charset="utf-8">
<title>Regenerative Wellness and Cell Factor Therapy – Quenmora Wellness</title>
<link rel="stylesheet" href="https://fonts.googleapis.com/css2?family=Exo+2:ital,wght@0,500;0,700;0,800;1,500&family=Fira+Sans:wght@400;500&display=swap">
<style>
  :root {
    --backdrop: #c9c9c9;
    --paper: #ffffff;
    --navy: #0054AA;
    --blue: #0677BA;
    --sky: #7BADD7;
    --mist: #CADEEF;
    --haze: #E8F1F8;
    --teal: #00AB8E;
    --teal-soft: #00BBA5;
    --mint: #67D7C9;
    --mint-pale: #C6EFE9;
    --ink: #111111;
  }
  * { box-sizing: border-box; margin: 0; padding: 0; }
  html, body {
    width: 1200px;
    height: 1200px;
    overflow: hidden;
    background: var(--backdrop);
  }
  .flyer {
    position: absolute;
    left: 232px;
    top: 80px;
    width: 735px;
    height: 1040px;
    background: var(--paper);
    overflow: hidden;
    font-family: "Fira Sans", sans-serif;
    color: var(--ink);
  }
  .flyer__shapes {
    position: absolute;
    inset: 0;
    width: 735px;
    height: 1040px;
  }
  .flyer__title {
    position: absolute;
    left: 52px;
    top: 142px;
    font-family: "Exo 2", sans-serif;
    font-weight: 800;
    font-size: 34px;
    line-height: 41px;
    letter-spacing: 0.6px;
    color: var(--navy);
    text-transform: uppercase;
  }
  .brand {
    position: absolute;
    left: 400px;
    top: 62px;
    width: 312px;
    text-align: center;
  }
  .brand__disc {
    width: 216px;
    height: 216px;
    margin: 0 auto;
    border-radius: 50%;
    background: var(--mint-pale);
  }
  .brand__name {
    margin-top: 16px;
    font-family: "Exo 2", sans-serif;
    font-weight: 700;
    font-size: 25px;
    color: var(--teal);
  }
  .benefits {
    position: absolute;
    left: 52px;
    top: 414px;
    width: 380px;
  }
  .benefit { margin-bottom: 44px; }
  .benefit__heading {
    position: relative;
    padding-left: 25px;
    font-family: "Exo 2", sans-serif;
    font-weight: 800;
    font-size: 17.5px;
    line-height: 24px;
    text-transform: uppercase;
    color: var(--ink);
  }
  .benefit__heading::before {
    content: "";
    position: absolute;
    left: 0;
    top: 1px;
    width: 10px;
    height: 23px;
    background: var(--navy);
  }
  .benefit__text {
    margin-top: 12px;
    font-size: 14.2px;
    line-height: 18.2px;
    color: var(--ink);
  }
  .cta {
    position: absolute;
    left: 0;
    top: 917px;
    width: 528px;
    height: 75px;
    padding: 18px 0 0 52px;
    background: var(--mist);
    mix-blend-mode: multiply;
    font-family: "Exo 2", sans-serif;
  }
  .cta__limit {
    font-weight: 800;
    font-size: 18px;
    line-height: 20px;
    text-transform: uppercase;
  }
  .cta__call {
    font-weight: 500;
    font-size: 18px;
    line-height: 22px;
  }
  .cta__call em { font-style: italic; text-transform: uppercase; }
  .qr-slot {
    position: absolute;
    left: 318px;
    top: 922px;
    width: 64px;
    height: 64px;
    background: var(--paper);
    border: 3px solid var(--navy);
  }
</style>
</head>
<body>
  <main class="flyer">
    <svg class="flyer__shapes" viewBox="0 0 735 1040">
      <defs>
        <linearGradient id="meditation-tones" x1="0" y1="0" x2="0" y2="1">
          <stop offset="0" stop-color="var(--haze)"/>
          <stop offset="0.45" stop-color="var(--mist)"/>
          <stop offset="0.55" stop-color="var(--sky)"/>
          <stop offset="1" stop-color="var(--blue)"/>
        </linearGradient>
      </defs>
      <polygon class="accent-wedge" fill="var(--teal)"
        points="294,372 735,445 735,1040 366,1040 527,489"/>
      <g role="img" aria-label="Photo of a woman meditating cross-legged on a mat in a grassy field">
        <polygon fill="url(#meditation-tones)" points="735,489 500,701 735,1032"/>
      </g>
    </svg>

    <h1 class="flyer__title">Regenerative<br>Wellness and Cell<br>Factor Therapy</h1>

    <div class="brand">
      <div class="brand__disc"></div>
      <p class="brand__name">Quenmora Wellness</p>
    </div>

    <section class="benefits">
      <article class="benefit">
        <h2 class="benefit__heading">Regenerate &amp; Repair Tissue</h2>
        <p class="benefit__text">Lorem ipsum dolor sit amet, consectetuer adipiscing elit, sed diam nonummy nibh euismod tincidunt ut laoreet dolore magna aliquam erat volutpat. Ut wisi enim ad minim veniam, quis nostrud exerci tation ullamcorper suscipit lobortis nisl ut aliquip</p>
      </article>
      <article class="benefit">
        <h2 class="benefit__heading">Decrease Pain &amp; Soreness</h2>
        <p class="benefit__text">Lorem ipsum dolor sit amet, consectetuer adipiscing elit, sed diam nonummy nibh euismod tincidunt ut laoreet dolore magna aliquam erat volutpat. Ut wisi enim ad minim veniam, quis nostrud exerci tation ullamcorper suscipit lobortis nisl ut aliquip</p>
      </article>
      <article class="benefit">
        <h2 class="benefit__heading">Improve Your Health</h2>
        <p class="benefit__text">Lorem ipsum dolor sit amet, consectetuer adipiscing elit, sed diam nonummy nibh euismod tincidunt ut laoreet dolore magna aliquam erat volutpat. Ut wisi enim ad minim veniam, quis nostrud exerci tation ullamcorper suscipit lobortis nisl ut aliquip</p>
      </article>
    </section>

    <aside class="cta">
      <p class="cta__limit">Seating is limited</p>
      <p class="cta__call"><em>Call today!</em> (555) 214-7830</p>
    </aside>
    <div class="qr-slot" role="img" aria-label="QR code linking to the landing page"></div>
  </main>
</body>
</html>
```